Spray Foam Company Business Card

We need a business card designed for our spray foam insulation and roof coatings business. We handle residential and commercial projects.
Industry/Entity Type
Construction
Contact Information for Business Card
We would like it to say:
K & R Coat
with these bullet points
-foam insulation
-waterproofing roof system
-water proofing foundation systems
website is krcoatfoamsealers.com (this was just purchased)
office phone : 630-555-0148
And 3 cards with names on them the names are :
Darren Hollis
Trevor Lindqvist
Neil Bruxton
maybe the bullet points can go on the back?
if you go this website it is another division of our company and you can see the font we use in the K & R. We do not want to use the same half circles that it has just the lettering
www.thesturdiestfinishwork.com
Look and feel
Each slider illustrates characteristics of the customer's brand and the style your logo design should communicate.

```html
<!DOCTYPE html>
<html lang="en">
<head>
<meta charset="utf-8">
<title>K &amp; R Coat — Business Cards</title>
<link rel="stylesheet" href="https://fonts.googleapis.com/css2?family=Jost:wght@400;500;600&display=swap">
<style>
  :root {
    --bg: #d9d9d9;
    --paper: #ffffff;
    --blue: #3f5cab;
    --violet: #4b2a6c;
    --crimson: #a92b2c;
    --flame: #e0522b;
    --gold: #dcb22e;
    --ink-phone: #d0582d;
    --ink-web: #8a2a3c;
    --ink-list: #4b2a6c;
    --icon: #dba52a;
    --brand-gradient: linear-gradient(90deg, var(--blue) 0%, var(--violet) 25%, var(--crimson) 55%, var(--flame) 78%, var(--gold) 100%);
  }
  * { box-sizing: border-box; margin: 0; padding: 0; }
  html, body { width: 1200px; height: 1000px; overflow: hidden; }
  body {
    background: var(--bg);
    font-family: "Jost", "Century Gothic", sans-serif;
    position: relative;
  }
  .card-sheet {
    position: absolute;
    left: 80px; top: 190px;
    display: grid;
    grid-template-columns: 500px 500px;
    grid-template-rows: 286px 286px;
    gap: 40px;
  }
  .card {
    width: 500px; height: 286px;
    background: var(--paper);
    position: relative;
    overflow: hidden;
    box-shadow: 0 6px 16px rgba(0,0,0,0.25);
  }
  .card--front {
    background: var(--brand-gradient);
    display: flex; align-items: center; justify-content: center;
  }
  .brand-name {
    color: #fff;
    font-weight: 500;
    font-size: 78px;
    letter-spacing: 2px;
  }
  .card__band {
    height: 72px;
    background: var(--brand-gradient);
    display: flex; align-items: center; justify-content: space-between;
    padding: 0 22px 0 18px;
  }
  .band-mark {
    color: #fff; font-weight: 500; font-size: 20px; letter-spacing: 1px;
  }
  .person-name {
    color: #fff; font-weight: 600; font-size: 27px;
    letter-spacing: 1.5px; text-transform: uppercase;
  }
  .contact {
    list-style: none;
    margin-top: 14px;
    padding-right: 22px;
    text-align: right;
    font-size: 18px;
    letter-spacing: 1.4px;
  }
  .contact li { display: flex; justify-content: flex-end; align-items: center; gap: 12px; height: 28px; }
  .contact__phone { color: var(--ink-phone); }
  .contact__web { color: var(--ink-web); }
  .contact svg { width: 18px; height: 18px; flex: none; }
  .services {
    position: absolute; left: 26px; bottom: 26px;
    list-style: none;
    color: var(--ink-list);
    font-size: 16px; line-height: 21px;
  }
  .services li::before {
    content: "•"; color: var(--blue); margin-right: 7px;
  }
</style>
</head>
<body>
  <main class="card-sheet">
    <section class="card card--front" aria-label="Card front">
      <span class="brand-name">K &amp; R Coat</span>
    </section>

    <section class="card card--person">
      <header class="card__band">
        <span class="band-mark">K &amp; R</span>
        <h2 class="person-name">Neil Bruxton</h2>
      </header>
      <ul class="contact">
        <li class="contact__phone">630-555-0148
          <svg viewBox="0 0 24 24" aria-hidden="true"><path fill="var(--icon)" d="M6.6 10.8a15 15 0 0 0 6.6 6.6l2.2-2.2a1 1 0 0 1 1-.25 11.4 11.4 0 0 0 3.6.57 1 1 0 0 1 1 1V20a1 1 0 0 1-1 1A17 17 0 0 1 3 4a1 1 0 0 1 1-1h3.5a1 1 0 0 1 1 1c0 1.25.2 2.45.57 3.57a1 1 0 0 1-.25 1z"/></svg>
        </li>
        <li class="contact__web">krcoatfoamsealers.com
          <svg viewBox="0 0 24 24" aria-hidden="true"><g fill="none" stroke="var(--icon)" stroke-width="2"><circle cx="12" cy="12" r="10"/><ellipse cx="12" cy="12" rx="4" ry="10"/><path d="M2 12h20M4 7h16M4 17h16"/></g></svg>
        </li>
      </ul>
      <ul class="services">
        <li>foam insulation</li>
        <li>waterproofing roof system</li>
        <li>water proofing foundation systems</li>
      </ul>
    </section>

    <section class="card card--person">
      <header class="card__band">
        <span class="band-mark">K &amp; R</span>
        <h2 class="person-name">Darren Hollis</h2>
      </header>
      <ul class="contact">
        <li class="contact__phone">630-555-0148
          <svg viewBox="0 0 24 24" aria-hidden="true"><path fill="var(--icon)" d="M6.6 10.8a15 15 0 0 0 6.6 6.6l2.2-2.2a1 1 0 0 1 1-.25 11.4 11.4 0 0 0 3.6.57 1 1 0 0 1 1 1V20a1 1 0 0 1-1 1A17 17 0 0 1 3 4a1 1 0 0 1 1-1h3.5a1 1 0 0 1 1 1c0 1.25.2 2.450.57 3.57a1 1 0 0 1-.25 1z"/></svg>
        </li>
        <li class="contact__web">krcoatfoamsealers.com
          <svg viewBox="0 0 24 24" aria-hidden="true"><g fill="none" stroke="var(--icon)" stroke-width="2"><circle cx="12" cy="12" r="10"/><ellipse cx="12" cy="12" rx="4" ry="10"/><path d="M2 12h20M4 7h16M4 17h16"/></g></svg>
        </li>
      </ul>
      <ul class="services">
        <li>foam insulation</li>
        <li>waterproofing roof system</li>
        <li>water proofing foundation systems</li>
      </ul>
    </section>

    <section class="card card--person">
      <header class="card__band">
        <span class="band-mark">K &amp; R</span>
        <h2 class="person-name">Trevor Lindqvist</h2>
      </header>
      <ul class="contact">
        <li class="contact__phone">630-555-0148
          <svg viewBox="0 0 24 24" aria-hidden="true"><path fill="var(--icon)" d="M6.6 10.8a15 15 0 0 0 6.6 6.6l2.2-2.2a1 1 0 0 1 1-.25 11.4 11.4 0 0 0 3.6.57 1 1 0 0 1 1 1V20a1 1 0 0 1-1 1A17 17 0 0 1 3 4a1 1 0 0 1 1-1h3.5a1 1 0 0 1 1 1c0 1.25.2 2.45.57 3.57a1 1 0 0 1-.25 1z"/></svg>
        </li>
        <li class="contact__web">krcoatfoamsealers.com
          <svg viewBox="0 0 24 24" aria-hidden="true"><g fill="none" stroke="var(--icon)" stroke-width="2"><circle cx="12" cy="12" r="10"/><ellipse cx="12" cy="12" rx="4" ry="10"/><path d="M2 12h20M4 7h16M4 17h16"/></g></svg>
        </li>
      </ul>
      <ul class="services">
        <li>foam insulation</li>
        <li>waterproofing roof system</li>
        <li>water proofing foundation systems</li>
      </ul>
    </section>
  </main>
</body>
</html>
```